Etiketten-Design für Glühwein/Kinderpunsch
Zielgruppe
wir sind ein konventioneller Landwirtschaftlicher Betrieb. Ein Standbein sind unsere 2ha große Heidelbeerplantage. wir haben eine 'beerige Produktpalette' und brauchen für die Saisonware Glühwein/Kinderpunsch neue Etiketten; Zielgruppe: Regionale Vermarkung, Direktvermakrtung, von 0-99,
Aufgabenstellung
peppiges, auffälliges Etiektt, das Lust auf Glühwein/Winter macht und für den alkoholfreie Fruchtpunsch was das Kinder und Erwachsene anspricht
Flaschenetiektt mit den gesetzlichen Vorgaben,
Farben: Unser Logo ist in Lila, hellgrün, dunkelgrün, schwarz und weiß gehalten, sind aber prinzipiell offen für alles

```html
<!DOCTYPE html>
<html lang="de">
<head>
<meta charset="utf-8">
<title>Hollerhain Genusswelt – Winteretiketten</title>
<link href="https://fonts.googleapis.com/css2?family=Jost:wght@700;800&display=swap" rel="stylesheet">
<style>
  :root {
    --page: #ffffff;
    --violet: #3f0aa8;
    --violet-deep: #2c0580;
    --violet-text: #a99be0;
    --blue: #1a2fa8;
    --blue-deep: #10207e;
    --blue-text: #a8b6f0;
    --green: #6fd21a;
    --white: #ffffff;
    --berry: #4b5ea8;
    --leaf: #5aa83a;
    --punch-red: #a4202a;
    --orange: #f2a01e;
  }
  * { margin: 0; padding: 0; box-sizing: border-box; }
  html, body {
    width: 780px; height: 1200px; overflow: hidden;
    background: var(--page);
    font-family: "Jost", "Futura", sans-serif;
  }
  .label-row {
    position: absolute; top: 335px; left: 62px;
    display: flex; gap: 70px;
  }
  .label {
    position: relative; width: 295px; height: 530px; overflow: hidden;
  }
  .label--gluehwein { background: var(--violet); }
  .label--punsch { background: var(--blue); }
  .winter-pattern {
    position: absolute; inset: 0 0 240px 0;
    background: radial-gradient(ellipse at 70% 40%, rgba(120,110,255,0.35), transparent 65%);
  }
  .label--gluehwein .winter-pattern {
    background: radial-gradient(ellipse at 70% 40%, rgba(140,90,255,0.35), transparent 65%), linear-gradient(var(--violet-deep), transparent 30%);
  }
  .label--punsch .winter-pattern {
    background: radial-gradient(ellipse at 70% 40%, rgba(60,110,255,0.4), transparent 65%), linear-gradient(var(--blue-deep), transparent 30%);
  }
  .brand {
    position: absolute; top: 78px; left: 0; right: 0;
    display: flex; flex-direction: column; align-items: center;
    color: var(--white); font-weight: 800; line-height: 1;
  }
  .brand-dot {
    width: 12px; height: 12px; border-radius: 50%;
    background: var(--green); margin-bottom: 8px;
  }
  .brand-name { font-size: 26px; letter-spacing: 0.5px; }
  .brand-sub { font-size: 13px; margin-top: 4px; letter-spacing: 0.5px; }
  .product-title {
    position: absolute; left: 0; right: 0; top: 162px;
    text-align: center; font-weight: 800;
    font-size: 37px; line-height: 50px; letter-spacing: 0.3px;
  }
  .label--gluehwein .product-title { color: var(--violet-text); }
  .label--punsch .product-title { color: var(--blue-text); }
  .badge-alkoholfrei {
    position: absolute; top: 265px; left: 72px;
    width: 144px; height: 30px; background: var(--green);
    color: var(--white); font-weight: 700; font-size: 15px;
    display: flex; align-items: center; justify-content: center;
    letter-spacing: 0.3px;
  }
  .product-photo { position: absolute; left: 0; right: 0; bottom: 0; }
  .label--gluehwein .product-photo {
    top: 275px;
    background: linear-gradient(110deg, transparent 0%, transparent 20%, rgba(90,168,58,0.7) 30%, var(--berry) 50%, rgba(164,60,110,0.8) 75%, rgba(200,130,170,0.7) 100%);
  }
  .label--punsch .product-photo {
    top: 290px;
    background: linear-gradient(100deg, var(--punch-red) 0%, #d2453a 45%, var(--orange) 70%, #9a5030 100%);
  }
</style>
</head>
<body>
  <main class="label-row">
    <section class="label label--gluehwein">
      <div class="winter-pattern" role="img" aria-label="Dekoratives Schneeflocken-Muster in Lila"></div>
      <div class="brand">
        <span class="brand-dot"></span>
        <span class="brand-name">Hollerhain</span>
        <span class="brand-sub">Genusswelt</span>
      </div>
      <h1 class="product-title">HEIDELBEER<br>GLÜHWEIN</h1>
      <div class="product-photo" role="img" aria-label="Foto: Heidelbeeren mit Blättern neben einem Glas Glühwein"></div>
    </section>

    <section class="label label--punsch">
      <div class="winter-pattern" role="img" aria-label="Dekoratives Schneeflocken-Muster in Blau"></div>
      <div class="brand">
        <span class="brand-dot"></span>
        <span class="brand-name">Hollerhain</span>
        <span class="brand-sub">Genusswelt</span>
      </div>
      <h1 class="product-title">FRUCHT<br>PUNSCH</h1>
      <div class="product-photo" role="img" aria-label="Foto: Glas Fruchtpunsch mit Orangenscheiben, halbierte Orange und Zimtstangen"></div>
      <div class="badge-alkoholfrei">ALKOHOLFREI</div>
    </section>
  </main>
</body>
</html>
```